Quillbrook Health needs a new services brochure

We need a new brochure that highlights the services that we offer at our clinic. We are a multidisciplinary health clinic that focuses on injury rehabilitation and pain management. We are looking for a brochure that will highlight our primary services to our clientele and inform potential clients of what we can offer. We pride ourselves on our quality of care and our advanced treatment techniques.
Target Market(s)
young families, athletes, people interested in their health.
Industry/Entity Type
Health And Wellness
Colors
Designer to choose colors to be used in the design.
Requirements
Must have
- We would love our new brochure to be a tri-fold that has 6 pages. We would like it to have brief information about our featured services:
- - Chiropractic
- - Massage Therapy
- - Manual Osteopathic Therapy
- - Acupuncture
- - Laser Therapy
- - Radial Shockwave Therapy
- We would also like this brochure to include a brief price list and direct billing info, About Us section & Contact information.
Nice to have
- If there is space to list that we also offer other services such as : Tissue Unwind Method, Hot Stone Massage, Cupping Technique, Pembrill Method, and Kinesiology Taping that would be great. We would like to use images similar to those that are on our website (we have hi-res of all images on the website) www.quillbrookhealth.ca and colours that would fit with our logo.

```html
<!DOCTYPE html>
<html lang="en">
<head>
<meta charset="utf-8">
<title>Quillbrook Health – Services Tri-fold</title>
<link href="https://fonts.googleapis.com/css2?family=Montserrat:wght@600;700&family=Open+Sans:wght@400;600;700&display=swap" rel="stylesheet">
<style>
:root{
  --blue:#1b74c9;
  --blue-dark:#0f5aa6;
  --blue-soft:#dcebf8;
  --ink:#3d4450;
  --muted:#7a828e;
  --paper:#ffffff;
  --stage:#eceff2;
  --rule:#d7dde4;
}
*{box-sizing:border-box;margin:0;padding:0}
html,body{width:769px;height:1200px;overflow:hidden;background:var(--stage)}
body{font-family:"Open Sans",Arial,sans-serif;color:var(--ink);font-size:8px;line-height:1.45}
.sheet{position:absolute;left:10px;width:749px;height:580px;background:var(--paper);display:grid;grid-template-columns:repeat(3,1fr);box-shadow:0 2px 8px rgba(0,0,0,.12)}
.sheet--outside{top:10px}
.sheet--inside{top:610px}
.panel{position:relative;padding:18px 16px;border-right:1px dashed var(--rule);overflow:hidden}
.panel:last-child{border-right:none}
h2,h3{font-family:"Montserrat",Arial,sans-serif;color:var(--blue)}
h2{font-size:16px;letter-spacing:.5px;margin-bottom:10px}
h3{font-size:9.5px;margin:10px 0 4px;display:flex;align-items:center;gap:6px}
.price-list{list-style:none}
.price-list li{display:flex;justify-content:space-between;border-bottom:1px dotted var(--rule);padding:2px 0}
.price-list li span:last-child{color:var(--blue-dark);font-weight:600}
.note{color:var(--muted);font-size:7.5px;margin-top:4px}
.info-box{background:var(--blue);color:#fff;padding:10px 12px;margin-top:12px}
.info-box h3{color:#fff;margin-top:0}
.info-box .price-list li{border-color:rgba(255,255,255,.35)}
.info-box .price-list li span:last-child{color:#fff}
.contact{margin-top:12px}
.contact p{display:flex;align-items:center;gap:6px;margin-bottom:4px}
.brand{display:flex;align-items:center;gap:7px;font-family:"Montserrat",Arial,sans-serif;font-weight:700;font-size:14px;color:var(--blue-dark);margin-bottom:4px}
.brand-dot{width:14px;height:14px;border-radius:50%;background:var(--blue)}
.brand-phone{color:var(--muted);font-size:8px;margin-bottom:10px}
.photo{background:linear-gradient(135deg,#cfe3f4,#8fb9de);display:block}
.cover-photo{height:200px;margin:0 -16px;position:relative}
.badge{position:absolute;right:18px;bottom:-22px;width:48px;height:48px;border-radius:50%;background:var(--blue-dark);border:3px solid #fff}
.about{margin-top:30px}
.about p{margin-bottom:6px}
.web-bar{position:absolute;left:0;right:0;bottom:0;background:var(--blue);color:#fff;font-weight:600;font-size:10px;text-align:center;padding:12px 0}
.services-photo{height:150px;margin:-18px -16px 8px;position:relative}
.services-title{position:absolute;left:16px;bottom:14px;background:var(--blue);color:#fff;font-family:"Montserrat",Arial,sans-serif;font-weight:700;font-size:15px;padding:4px 10px}
.num{flex:none;width:16px;height:16px;border-radius:50%;background:var(--blue);color:#fff;font-size:8px;display:flex;align-items:center;justify-content:center}
.service p{margin-bottom:4px}
.side-photo{position:absolute;left:0;right:0;bottom:0;height:150px}
</style>
</head>
<body>

<section class="sheet sheet--outside">
  <div class="panel">
    <h2>PRICING</h2>
    <h3>Massage Therapy</h3>
    <ul class="price-list">
      <li><span>30 Minutes</span><span>$55</span></li>
      <li><span>45 Minutes</span><span>$75</span></li>
      <li><span>60 Minutes</span><span>$90</span></li>
      <li><span>Infant Massage</span><span>$40</span></li>
      <li><span>Hot Stone Massage</span><span>$105</span></li>
    </ul>
    <h3>Acupuncture</h3>
    <ul class="price-list">
      <li><span>Initial Assessment</span><span>$85</span></li>
      <li><span>Follow-up Treatment</span><span>$65</span></li>
    </ul>
    <h3>Laser Therapy</h3>
    <ul class="price-list">
      <li><span>Initial Assessment</span><span>$80</span></li>
      <li><span>Subsequent Treatment</span><span>$50</span></li>
    </ul>
    <h3>Chiropractic</h3>
    <ul class="price-list">
      <li><span>Initial Visit – Adults</span><span>$90</span></li>
      <li><span>Follow-up – Adults</span><span>$55</span></li>
      <li><span>Students &amp; Seniors</span><span>$45</span></li>
      <li><span>Children under 12</span><span>$35</span></li>
    </ul>
    <p class="note">Prices include applicable taxes and may change without notice.</p>
  </div>

  <div class="panel">
    <h3>Manual Osteopathic Therapy</h3>
    <ul class="price-list">
      <li><span>Initial Assessment</span><span>$95</span></li>
      <li><span>Follow-up Treatment</span><span>$75</span></li>
    </ul>
    <h3>Radial Shockwave Therapy</h3>
    <ul class="price-list">
      <li><span>Per Session</span><span>$60</span></li>
      <li><span>Package of Five</span><span>$275</span></li>
    </ul>
    <h3>Direct Billing</h3>
    <p>We bill most extended health plans directly, so you only pay what your coverage does not. Ask our front desk to check your plan before your visit.</p>
    <div class="info-box">
      <h3>Opening Hours</h3>
      <ul class="price-list">
        <li><span>Monday</span><span>8am – 8pm</span></li>
        <li><span>Tuesday</span><span>8am – 8pm</span></li>
        <li><span>Wednesday</span><span>8am – 8pm</span></li>
        <li><span>Thursday</span><span>8am – 8pm</span></li>
        <li><span>Friday</span><span>8am – 6pm</span></li>
        <li><span>Saturday</span><span>9am – 3pm</span></li>
        <li><span>Sunday</span><span>Closed</span></li>
      </ul>
    </div>
    <div class="contact">
      <h3>Located at</h3>
      <p><svg width="10" height="12" viewBox="0 0 10 12"><path d="M5 0a4 4 0 0 0-4 4c0 3 4 8 4 8s4-5 4-8a4 4 0 0 0-4-4z" fill="#1b74c9"/><circle cx="5" cy="4" r="1.5" fill="#fff"/></svg>48 Larkspur Avenue, Suite 3</p>
      <p><svg width="10" height="10" viewBox="0 0 10 10"><path d="M2 0l2 2-1 1.5a6 6 0 0 0 3.5 3.5L8 6l2 2-1.5 2C4 10 0 6 0 1.5z" fill="#1b74c9"/></svg>(555) 014-2280</p>
    </div>
  </div>

  <div class="panel">
    <div class="brand"><span class="brand-dot"></span>Quillbrook Health</div>
    <p class="brand-phone">(555) 014-2280</p>
    <div class="cover-photo photo" role="img" aria-label="Therapist treating a patient's shoulder in a bright clinic">
      <span class="badge"></span>
    </div>
    <div class="about">
      <h2>About Us</h2>
      <p>Quillbrook Health is a multidisciplinary clinic focused on injury rehabilitation and pain management for families, athletes and anyone who cares about their health.</p>
      <p>Our team combines quality care with advanced treatment techniques to help you move better and feel stronger.</p>
    </div>
    <div class="web-bar">www.quillbrookhealth.ca</div>
  </div>
</section>

<section class="sheet sheet--inside">
  <div class="panel">
    <div class="services-photo photo" role="img" aria-label="Therapist stretching a patient's leg on a treatment table">
      <span class="services-title">OUR SERVICES</span>
    </div>
    <div class="service">
      <h3><span class="num">1</span>Chiropractic</h3>
      <p>Chiropractic care is the assessment, treatment and prevention of musculoskeletal disorders. Gentle adjustments restore joint motion, ease pain and support the nervous system.</p>
      <p>Our chiropractors build a plan around your goals, whether you are recovering from injury or keeping active.</p>
    </div>
    <div class="service">
      <h3><span class="num">2</span>Massage Therapy</h3>
      <p>Massage therapy treats the soft tissues of the body to relieve tension, improve circulation and speed recovery. Sessions suit everyone from infants to athletes.</p>
    </div>
  </div>

  <div class="panel">
    <div class="service">
      <h3><span class="num">3</span>Manual Osteopathic Therapy</h3>
      <p>A hands-on approach that looks at the whole body, using gentle techniques to restore balance and mobility to joints, muscles and connective tissue.</p>
    </div>
    <div class="service">
      <h3><span class="num">4</span>Acupuncture</h3>
      <p>Fine sterile needles are placed at specific points to reduce pain, calm inflammation and support natural healing. Treatments are relaxing and well tolerated.</p>
    </div>
    <div class="service">
      <h3><span class="num">5</span>Laser Therapy</h3>
      <p>Low-level laser light reaches deep into tissue to boost cell repair and reduce swelling. It is painless, quick and ideal for stubborn injuries.</p>
    </div>
    <div class="service">
      <h3><span class="num">6</span>Radial Shockwave Therapy</h3>
      <p>Acoustic pressure waves stimulate healing in chronic tendon and soft tissue conditions such as plantar fasciitis, tennis elbow and calcific shoulder pain.</p>
    </div>
  </div>

  <div class="panel">
    <div class="service">
      <h3><span class="num">7</span>Cupping Technique</h3>
      <p>Gentle suction lifts the tissue to release tightness and draw fresh blood flow to sore areas.</p>
    </div>
    <div class="service">
      <h3><span class="num">8</span>Tissue Unwind Method</h3>
      <p>Targeted movement with pressure frees adhesions in muscle and fascia to restore range of motion.</p>
    </div>
    <div class="service">
      <h3><span class="num">9</span>Hot Stone Massage</h3>
      <p>Smooth heated stones melt away deep tension and leave you fully relaxed.</p>
    </div>
    <div class="service">
      <h3><span class="num">10</span>Pembrill Method</h3>
      <p>Instrument-assisted soft tissue work that breaks down scar tissue and eases chronic strain.</p>
    </div>
    <div class="service">
      <h3><span class="num">11</span>Kinesiology Taping</h3>
      <p>Elastic tape supports muscles and joints while letting you stay active.</p>
    </div>
    <div class="side-photo photo" role="img" aria-label="Therapist massaging a patient's foot"></div>
  </div>
</section>

</body>
</html>
```